Visitenkarten
Zielgruppe
Hallo!
Für mein Unternehmen habe ich bereits einmal ein Logo mit Feldmotte erstellen lassen (leider weiß ich den Designer nicht mehr).
Unter meinem Unternehmen Vollmerhaus Coaching laufen zwei Unternehmensbereiche, für die ich jetzt Visitenkarten benötige. Daher ist der Stil der beiden Teilbereiche ähnlich. Die Logos existieren schon. Nun benötige ich für beide Bereiche Visitenkarten. Für beide Bereiche benötige ich im Anschluss im 1:1 Auftrage noch Dateien, damit die ich Logos auch gut auf Webseiten und Social Medien nutzen kann.
Vollmerhaus HR Services <: bietet HR Dienstleistungen rund um das Personalwesen an: HR-Trainings, HR Outsourcing und Projekt- und Interimsmanagement
Sattelklar Balance | Vollmerhaus Coaching: bietet Mental- und Hypnosecoachings an, Trainings zur mentalen Fitness, Stress- und Blockadenlösung im Reitsport und optimale Turniervorbereitung
Aufgabenstellung
Bitte den bestehenden Brandguide und die Materialien nutzen. Eigene Ideen sind willkommen, sollen aber in der Logik bleiben.
Daten Visitenkarte Vollmerhaus HR Services:
Annelie Vollmerhaus
Dipl. Sozialwirt, Business Coach, Mentaltrainer
Telefon +49 (0)1593 26 48 357
Mobil +49 (0)171 58 93 704
Mail: annelie@vollmerhaus-beratung.example
Vollmerhaus HR Services | Vollmerhaus Coaching
Am Lindenhang 9b
31582 Lindenfelde
Daten Visitenkarte Vollmerhaus Sattelklar Balance:
Dipl. Sozialwirt, Hypnosecoach, Mentaltrainer
Sattelklar Balance | Vollmerhaus Coaching

```html
<!DOCTYPE html>
<html lang="de">
<head>
<meta charset="utf-8">
<title>Visitenkarte – Annelie Vollmerhaus</title>
<link rel="stylesheet" href="https://fonts.googleapis.com/css2?family=Arimo:wght@400;700&display=swap">
<style>
  :root {
    --card-bg: #ffffff;
    --ink: #111111;
  }
  html, body {
    margin: 0;
    padding: 0;
    width: 1200px;
    height: 686px;
    overflow: hidden;
    background: var(--card-bg);
  }
  .card {
    position: relative;
    width: 1200px;
    height: 686px;
    background: var(--card-bg);
    color: var(--ink);
    font-family: "Arimo", Arial, sans-serif;
  }
  .name {
    position: absolute;
    left: 149px;
    top: 95px;
    margin: 0;
    font-size: 43px;
    font-weight: 700;
    letter-spacing: 0.21em;
    line-height: 1;
    text-transform: uppercase;
    white-space: nowrap;
  }
  .role {
    position: absolute;
    left: 150px;
    top: 178px;
    margin: 0;
    font-size: 31px;
    font-weight: 400;
    letter-spacing: 0.2em;
    line-height: 46px;
    text-transform: uppercase;
    white-space: nowrap;
  }
  .contact-labels,
  .contact-values {
    position: absolute;
    margin: 0;
    padding: 0;
    list-style: none;
    white-space: nowrap;
  }
  .contact-labels {
    left: 150px;
    top: 338px;
    font-size: 34px;
    letter-spacing: 0.07em;
    line-height: 50px;
  }
  .contact-values {
    left: 353px;
    top: 338px;
    line-height: 49px;
  }
  .contact-values li {
    height: 49px;
  }
  .phone {
    font-size: 34px;
    letter-spacing: 0.07em;
  }
  .text-line {
    font-size: 33px;
    letter-spacing: 0;
  }
  .contact-values a {
    color: inherit;
    text-decoration: none;
  }
</style>
</head>
<body>
  <main class="card">
    <h1 class="name">Annelie Vollmerhaus</h1>
    <p class="role">Dipl. Sozialwirt, Buisness Coach,<br>Mentaltrainer</p>

    <ul class="contact-labels">
      <li>Telefon</li>
      <li>Mobil</li>
      <li>Mail</li>
      <li>Ort</li>
    </ul>

    <ul class="contact-values">
      <li class="phone">+49 (0)1593 26 48 357</li>
      <li class="phone">+49 (0)171 58 93 704</li>
      <li class="text-line"><a href="mailto:annelie@vollmerhaus-beratung.example">annelie@vollmerhaus-beratung.example</a></li>
      <li class="text-line">Am Lindenhang 9b</li>
      <li class="text-line">31582 Lindenfelde</li>
    </ul>
  </main>
</body>
</html>
```